Flyer für Lach- und Humorworkshops
Zielgruppe
Ich biete Lach- und Humorworkshops an für Unternehmen und Privatpersonen, für mehr Lebensfreude und Erfolg, ob privat oder im Business.
Aufgabenstellung
- DIN A6
- Textvorgabe im Word kann auch gekürzt werden, je nach Platz auf dem Flyer
- Schlagwörter wie 'Lachen' in der Schrift 'Licorice' so wie auf der Website

```html
<!DOCTYPE html>
<html lang="de">
<head>
<meta charset="utf-8">
<title>Lach-Workshop Flyer</title>
<link href="https://fonts.googleapis.com/css2?family=Quicksand:wght@300;500;700&family=Amatic+SC:wght@700&family=Licorice&display=swap" rel="stylesheet">
<style>
  :root {
    --page: #ecebe8;
    --paper: #ffffff;
    --ink: #1d1d1d;
    --gold: #dcac58;
    --gold-dark: #8a7552;
    --cream: #f2e2bf;
    --text-light: #ffffff;
    --photo-light: #d6dadd;
    --photo-dark: #6d655c;
  }
  * { margin: 0; padding: 0; box-sizing: border-box; }
  html, body { width: 1200px; height: 1200px; overflow: hidden; }
  body {
    background: var(--page);
    font-family: "Quicksand", sans-serif;
    position: relative;
  }

  /* ---------- Front side ---------- */
  .flyer-front-wrap {
    position: absolute;
    left: 40px; top: 218px;
    width: 540px; height: 764px;
  }
  .flyer-front {
    position: absolute;
    left: 0; top: 0;
    width: 680px; height: 965px;
    transform: scale(0.794);
    transform-origin: 0 0;
    background: var(--paper);
    overflow: hidden;
    color: var(--text-light);
  }
  .flyer-front .shapes { position: absolute; inset: 0; }

  .brand-name {
    position: absolute;
    left: 22px; top: 38px;
    font-family: "Quicksand", sans-serif;
    font-weight: 300;
    font-size: 72px;
    letter-spacing: 1px;
    color: var(--gold);
  }
  .headline {
    position: absolute;
    left: 28px; top: 396px;
    font-family: "Amatic SC", cursive;
    font-weight: 700;
    font-size: 38px;
    letter-spacing: 3px;
    color: var(--gold);
  }
  .info-text {
    position: absolute;
    left: 12px; top: 478px;
    width: 378px;
    text-align: center;
    font-size: 14.6px;
    line-height: 20.2px;
    font-weight: 500;
  }
  .info-text h3 { font-size: 14.6px; font-weight: 700; }
  .info-text p { margin-bottom: 14px; }
  .info-text strong { font-weight: 700; }

  .topics {
    position: absolute;
    left: 398px; top: 712px;
    width: 282px;
    list-style: none;
    color: var(--ink);
    font-weight: 700;
    font-size: 18px;
    line-height: 25px;
    text-align: center;
  }
  .topics li { position: relative; }
  .topics li::before {
    content: "";
    position: absolute;
    left: 0; top: 10px;
    width: 6px; height: 6px;
    border-radius: 50%;
    background: var(--ink);
  }
  .registration {
    position: absolute;
    left: 520px; top: 858px;
    color: var(--ink);
    text-align: center;
    width: 150px;
  }
  .registration .label {
    font-size: 12px; font-weight: 500; letter-spacing: 2px;
  }
  .registration .phone {
    font-size: 17px; font-weight: 700; margin-top: 4px;
  }
  .web-pill {
    position: absolute;
    left: 462px; top: 920px;
    width: 190px; height: 25px;
    border-radius: 13px;
    background: var(--ink);
    color: var(--text-light);
    font-size: 13.5px;
    font-weight: 700;
    line-height: 25px;
    padding-left: 16px;
  }

  /* ---------- Back side ---------- */
  .flyer-back {
    position: absolute;
    left: 620px; top: 218px;
    width: 540px; height: 764px;
    background: var(--paper);
    overflow: hidden;
  }
  .laugh-artwork {
    position: absolute;
    left: 0; top: 170px;
    width: 540px; height: 423px;
    background: linear-gradient(100deg, #c9dcdc 0%, #efd9cf 35%, #f3dcd2 70%, #e6e8e4 100%);
  }
  .quote {
    position: absolute;
    left: 250px; top: 230px;
    width: 290px;
    text-align: center;
    font-family: "Licorice", cursive;
    font-size: 66px;
    line-height: 70px;
    color: var(--ink);
  }
</style>
</head>
<body>

<section class="flyer-front-wrap">
  <div class="flyer-front">
    <svg class="shapes" width="680" height="965" viewBox="0 0 680 965" xmlns="http://www.w3.org/2000/svg">
      <defs>
        <linearGradient id="barGradient" x1="0" y1="1" x2="1" y2="0">
          <stop offset="0" stop-color="#d8b168"/>
          <stop offset="1" stop-color="#6e6150"/>
        </linearGradient>
        <linearGradient id="creamGradient" x1="0" y1="0" x2="0" y2="1">
          <stop offset="0" stop-color="#d9ae62"/>
          <stop offset="1" stop-color="#f6ead0"/>
        </linearGradient>
        <linearGradient id="photoGradient" x1="0" y1="0" x2="0" y2="1">
          <stop offset="0" stop-color="#d6dadd"/>
          <stop offset="0.55" stop-color="#b9aa9a"/>
          <stop offset="1" stop-color="#4d4a45"/>
        </linearGradient>
      </defs>

      <!-- dark diagonal field -->
      <polygon points="0,152 680,795 680,965 0,965" fill="var(--ink)"/>

      <!-- gold accent bars -->
      <line x1="300" y1="88" x2="390" y2="12" stroke="url(#barGradient)" stroke-width="74" stroke-linecap="round"/>
      <line x1="12" y1="212" x2="100" y2="318" stroke="var(--gold)" stroke-width="30" stroke-linecap="round"/>

      <!-- cream crescent behind portrait -->
      <circle cx="560" cy="360" r="148" fill="url(#creamGradient)"/>

      <!-- main portrait -->
      <g role="img" aria-label="Porträtfoto der lachenden Workshopleiterin">
        <circle cx="465" cy="255" r="215" fill="url(#photoGradient)"/>
        <rect x="420" y="0" width="260" height="250" fill="#d6dadd"/>
      </g>

      <!-- small portrait top left -->
      <circle cx="148" cy="200" r="52" fill="#cfd1cf" role="img" aria-label="Kleines Foto einer lachenden Frau"/>

      <!-- gold circle -->
      <circle cx="600" cy="850" r="230" fill="var(--gold)"/>
      <circle cx="580" cy="595" r="75" fill="#e9d2a4" opacity="0.7"/>

      <!-- small portrait right -->
      <circle cx="546" cy="537" r="52" fill="#8f8a84" role="img" aria-label="Foto der Workshopleiterin im Lachen-Shirt"/>
    </svg>

    <div class="brand-name">lumora</div>
    <h2 class="headline">LASS UNS LACHEN</h2>

    <div class="info-text">
      <h3>Warum lachen?</h3>
      <p><strong>Lachen</strong> ist einfach, gesund und macht glücklich.<br>
      Lachen ist eine universelle Sprache, die verbindet.<br>
      Lachen ist sofort wirksam und nachhaltig zugleich.<br>
      Lachen ist ganzheitlich, nachhaltig und sinnvoll.</p>

      <h3>Lach-Workshop</h3>
      <p>Du suchst eine besondere Teambuilding Aktivität?
      Wie wäre es mit einer kurzen Auszeit aus dem Alltag, die lustig, gesund, nachhaltig und sinnvoll ist?<br>
      In einem Lach-Workshop geht es in erster Linie darum, gemeinsam Spass zu haben und ausgiebig zu lachen. Euch erwartet ein abwechslungsreicher Mix aus einfachen, spielerischen und kreativen Übungen.</p>

      <h3>Humor im Business – für ein positives Betriebsklima</h3>
      <p><strong>Lachen</strong> ist gesund – das gilt nicht nur für unsere persönliche Gesundheit, sondern auch für ein Unternehmen.</p>
    </div>

    <ul class="topics">
      <li>Teambuilding</li>
      <li>Persönlichkeitsentwicklung</li>
      <li>Stressmanagement</li>
      <li>Gesundheit &amp; Wohlbefinden</li>
      <li>Kreaktivität &amp; Innovation</li>
    </ul>

    <div class="registration">
      <div class="label">REGISTRATION:</div>
      <div class="phone">+49 1570 482 316</div>
    </div>

    <div class="web-pill">lachzeit-workshops.de</div>
  </div>
</section>

<section class="flyer-back">
  <div class="laugh-artwork" role="img" aria-label="Gemalte Illustration eines herzhaft lachenden Gesichts in Pastelltönen"></div>
  <p class="quote">Lachen<br>ist wie<br>Kurzferien.</p>
</section>

</body>
</html>
```